Design a professional business card for an accountant

I am a mid-career accountant and tax specialist. I am looking for a professional card design that would speak of the quality and trustworthiness of my services.

Keywords: accounting, tax, simple, professional, bold, white, committed, aspiring, detail-oriented

Information on card:
Nadim Khourbet
Accounting and Tax Consultant
+961 71 438 207
nadimkhourbet@velquarin.com

Final design submission should include editable files.

```html
<!DOCTYPE html>
<html lang="en">
<head>
<meta charset="utf-8">
<title>Nadim Khourbet — Business Card</title>
<link rel="stylesheet" href="https://fonts.googleapis.com/css2?family=Lato:wght@400;700&display=swap">
<style>
  :root {
    --backdrop: #1c1c1d;
    --card-white: #f1f2f4;
    --ink: #4a4a4c;
    --navy: #192a57;
    --navy-ink: #ffffff;
  }
  * { box-sizing: border-box; margin: 0; padding: 0; }
  html, body {
    width: 1200px;
    height: 900px;
    overflow: hidden;
    background: var(--backdrop);
    font-family: "Lato", sans-serif;
  }
  .sheet {
    width: 1200px;
    height: 900px;
    display: flex;
    flex-direction: column;
    align-items: center;
    justify-content: center;
    gap: 60px;
  }
  .card {
    width: 630px;
    height: 360px;
    position: relative;
    overflow: hidden;
  }

  /* Front */
  .card--front { background: var(--card-white); color: var(--ink); }
  .identity {
    position: absolute;
    left: 50px;
    top: 112px;
  }
  .identity__name {
    font-size: 25px;
    font-weight: 400;
    letter-spacing: 1px;
    text-transform: uppercase;
    padding-bottom: 3px;
    border-bottom: 2px solid var(--ink);
  }
  .identity__role {
    font-size: 13.5px;
    margin-top: 4px;
    letter-spacing: 0.3px;
  }
  .divider {
    position: absolute;
    left: 288px;
    top: 96px;
  }
  .contacts {
    position: absolute;
    left: 338px;
    top: 124px;
    list-style: none;
    font-size: 14.5px;
  }
  .contacts__item {
    display: flex;
    align-items: center;
    gap: 9px;
    margin-bottom: 8px;
  }
  .contacts__icon { flex: none; }

  /* Back */
  .card--back { background: var(--navy); color: var(--navy-ink); }
  .back__name {
    position: absolute;
    top: 150px;
    left: 0;
    width: 100%;
    text-align: center;
    font-size: 28px;
    font-weight: 400;
    letter-spacing: 2px;
    text-transform: uppercase;
  }
  .back__tagline {
    position: absolute;
    left: 0;
    right: 0;
    top: 262px;
    display: flex;
    align-items: center;
    gap: 14px;
    font-size: 14px;
    letter-spacing: 0.6px;
    white-space: nowrap;
  }
  .back__rule { height: 1px; background: var(--navy-ink); }
  .back__rule--left { width: 205px; }
  .back__rule--right { flex: 1; }
</style>
</head>
<body>
<main class="sheet">
  <section class="card card--front">
    <div class="identity">
      <h1 class="identity__name">Nadim Khourbet</h1>
      <p class="identity__role">Accounting and Tax Consultant</p>
    </div>
    <svg class="divider" width="40" height="160" viewBox="0 0 40 160" aria-hidden="true">
      <line x1="6" y1="0" x2="6" y2="160" stroke="#4a4a4c" stroke-width="2.5"/>
      <line x1="22" y1="22" x2="22" y2="130" stroke="#4a4a4c" stroke-width="2.5"/>
    </svg>
    <ul class="contacts">
      <li class="contacts__item">
        <svg class="contacts__icon" width="14" height="14" viewBox="0 0 14 14" aria-hidden="true">
          <rect width="14" height="14" rx="3" fill="#4a4a4c"/>
          <path d="M4.2 3.3c.4-.3.8-.2 1 .2l.7 1.3c.2.4.1.7-.2.9l-.5.4c.4 1 1.2 1.8 2.2 2.3l.4-.5c.3-.3.6-.4.9-.2l1.3.7c.4.2.5.6.2 1l-.6.7c-.4.4-1 .5-1.6.3C6.2 9.7 4.3 7.8 3.6 5.9c-.2-.6-.1-1.2.3-1.6z" fill="#f1f2f4"/>
        </svg>
        <span>+961 71 438 207</span>
      </li>
      <li class="contacts__item">
        <svg class="contacts__icon" width="14" height="14" viewBox="0 0 14 14" aria-hidden="true">
          <rect width="14" height="14" rx="3" fill="#4a4a4c"/>
          <rect x="3" y="4.2" width="8" height="5.6" rx="0.6" fill="none" stroke="#f1f2f4" stroke-width="1"/>
          <path d="M3.3 4.6 7 7.4l3.7-2.8" fill="none" stroke="#f1f2f4" stroke-width="1"/>
        </svg>
        <span>nadimkhourbet@velquarin.com</span>
      </li>
    </ul>
  </section>

  <section class="card card--back">
    <h2 class="back__name">Nadim Khourbet</h2>
    <div class="back__tagline">
      <span class="back__rule back__rule--left"></span>
      <span class="back__role">Accounting and Tax Consultant</span>
      <span class="back__rule back__rule--right"></span>
    </div>
  </section>
</main>
</body>
</html>
```